Web Design Project - Order A Moving Box for President Halvern (the product (box) has been designed

Create a web site design for a politically oriented project with an e-commerce function.

The webite will most likely only need to be 4 or 5 pages at the most; with one of those being an order page.

Please email with any questions.

Designers,

We have uploaded a excel file containing content and ideas.
We don;t have the product art back yet but you can leave a space on the "THe Box" page and the "Home" page.
Please email is you have any questions.

Thanks,
Dorin

Extension was added t allow more participation and updates from designers.

Target Market(s)

Conservation Voters, People who believe in the US Constitution, Capitalist, Entrepreneurs, Business Owners, Those who want to repeal HalvernCare

Industry/Entity Type

E-Commerce

Requirements
Must have
• Home Page
A Purpose and Mission Page (We have the content)
An order page

We have an outline of information that needs to be included.
You can email us directly at dorin@driftpack-away.com and we can forward the sketches and type for the site.
Nice to have
• 1. Links to a few (2 or 3)video clips if possible (will provide)
2. Links to voter registration website (will provide link)
3. Links to 4 or 5 other websites.

```html
<!DOCTYPE html>
<html lang="en">
<head>
<meta charset="utf-8">
<title>Buck Stops with You "Mr. President"</title>
<link href="https://fonts.googleapis.com/css2?family=Pathway+Gothic+One&family=Source+Sans+3:wght@400;600&display=swap" rel="stylesheet">
<style>
  :root {
    --ink: #1e1e1e;
    --accent: #f25a1d;
    --band-light: #f0f0f1;
    --band-grey: #d4d4d6;
    --rule: #555;
    --order-green: #a9d58c;
    --paper: #ffffff;
  }
  * { box-sizing: border-box; margin: 0; padding: 0; }
  html, body { width: 1200px; height: 874px; overflow: hidden; background: var(--paper); }
  body { position: relative; font-family: "Source Sans 3", sans-serif; color: var(--ink); }
  .top-bar { position: absolute; left: 0; top: 0; width: 1200px; height: 7px; background: #000; }

  .main-nav { position: absolute; top: 30px; left: 598px; display: flex; gap: 6px; }
  .main-nav a {
    display: block; height: 33px; line-height: 33px; text-align: center;
    font-size: 12px; color: var(--ink); text-decoration: none;
    background: linear-gradient(#fbfbfb, #e8e8e8);
    border: 1px solid #d2d2d2; border-radius: 9px;
    box-shadow: 0 4px 5px rgba(0,0,0,.22);
  }
  .nav-home { width: 90px; } .nav-box { width: 90px; }
  .nav-purpose { width: 136px; } .nav-order { width: 90px; }

  .title-band { position: absolute; left: 157px; top: 90px; width: 886px; height: 46px;
    background: var(--band-light); text-align: center; }
  .title-band h1 { font-family: "Pathway Gothic One", sans-serif; font-weight: 400;
    font-size: 29px; line-height: 46px; }
  .sub-band { position: absolute; left: 157px; top: 136px; width: 886px; height: 58px;
    background: var(--band-grey); text-align: center; font-size: 13.5px; padding-top: 11px; }

  .hero { position: absolute; left: 314px; top: 176px; width: 561px; height: 291px;
    border: 1px solid #bbb; background: #fff; padding: 3px;
    box-shadow: 0 10px 8px -6px rgba(0,0,0,.55); }
  .hero-art { width: 100%; height: 100%;
    background: linear-gradient(180deg, #f4f4f4 0%, #e9e9e9 45%, #a9d98c 75%, #9a9a9a 100%); }

  .pitch { position: absolute; top: 500px; font-family: "Pathway Gothic One", sans-serif;
    font-size: 23px; line-height: 32px; text-align: center; }
  .pitch-left { left: 178px; width: 336px; }
  .pitch-right { left: 552px; width: 462px; }
  .divider { position: absolute; border-left: 1px dotted var(--rule); }
  .divider-pitch { left: 533px; top: 508px; height: 46px; }
  .divider-body { left: 627px; top: 591px; height: 143px; }

  .intro { position: absolute; left: 178px; top: 585px; width: 400px; font-size: 11.5px;
    line-height: 20.3px; text-align: justify; }
  .highlight { color: var(--accent); }
  .intro .highlight { margin-top: 5px; }

  .box-facts { position: absolute; left: 674px; top: 586px; width: 360px; list-style: none;
    font-size: 11.5px; line-height: 18.5px; }
  .box-facts li { position: relative; padding-left: 16px; margin-bottom: 6px; }
  .box-facts li::before { content: ""; position: absolute; left: 0; top: 7px;
    border-left: 4px solid #333; border-top: 2.5px solid transparent; border-bottom: 2.5px solid transparent; }
  .box-facts .highlight { display: block; }

  .order-panel { position: absolute; left: 166px; top: 754px; width: 866px; height: 85px;
    border: 1px solid #cfcfcf; box-shadow: 0 1px 4px rgba(0,0,0,.15);
    padding: 10px 16px; font-size: 11.5px; line-height: 20.3px; }
  .order-button { position: absolute; left: 893px; top: 822px; width: 114px; height: 32px;
    background: var(--order-green); color: var(--ink); font-size: 13px; line-height: 32px;
    text-align: center; text-decoration: none; }
</style>
</head>
<body>
  <div class="top-bar"></div>

  <nav class="main-nav">
    <a class="nav-home" href="#">Home</a>
    <a class="nav-box" href="#">The Box</a>
    <a class="nav-purpose" href="#">The Purpose &amp; Mission</a>
    <a class="nav-order" href="#">Order</a>
  </nav>

  <header>
    <div class="title-band"><h1>Buck Stops with You "Mr. President"</h1></div>
    <div class="sub-band">Order a Box, Send a Message and Feed Hungry Kids.</div>
  </header>

  <figure class="hero">
    <div class="hero-art" role="img" aria-label="Cartoon of movers in orange loading the first family's belongings from the presidential residence into an orange moving truck headed to a welcome sign of their home city"></div>
  </figure>

  <h2 class="pitch pitch-left">It’s time to tell the HALVERN's &nbsp; to start packing<br>by sending them &nbsp; a MOVING box today!!!</h2>
  <div class="divider divider-pitch"></div>
  <h2 class="pitch pitch-right">Place your order and have this custom designed moving box sent<br>directly &nbsp;to 1200 Meridian Avenue Yes, the Executive Residence…</h2>

  <section class="intro">
    <p>Let's make sure the Halvern's and the rest of the main stream media get the message we are ready for some of that "HOPE &amp; CHANGE" he's always talking about. &nbsp;It's time to CHANGE the resident at the Executive Residence and we HOPE they'll be packed up and out come January 2013!.</p>
    <p class="highlight">For US, &nbsp;it can't come some enough!!!</p>
  </section>

  <div class="divider divider-body"></div>

  <ul class="box-facts">
    <li>This small box will easily hold ALL of Barrett's accomplishments.<span class="highlight">Oh wait, we forgot, there aren't any!</span></li>
    <li style="margin-bottom:0">But it is just too small to hold Marisol's new $6,800 shirt.</li>
    <li style="margin-bottom:0">It's too small to hold all the gifts from the Sunvane executives.</li>
    <li>But it will hold all the souvenirs from his trip to Israel<span class="highlight">Oh we forgot, This President has never ever been!</span></li>
    <li>and of course, the box is much too small to contain his EGO.</li>
  </ul>

  <section class="order-panel">
    <p>For only &nbsp;$9.75 &nbsp;you can have a moving box sent &nbsp;to the Halvern's. &nbsp;Your box will be sent First Class Mail, which will also help prop up the failing National Post Service, in addition to sending your message of "Hope For Change" to the current Executive Residence resident, your purchase of CLICK TO one box will provide enough food to feed a nutrious meal to 6 starving children.</p>
  </section>
  <a class="order-button" href="#">Click to Order Now</a>
</body>
</html>
```